New Business Card Design Project

Would like you to take my logo and create a business card much like the Bramwell leasing.
I can get you the fonts used for the back of the card.
I want the same speckled blue with my logo on it.

Feel free to improve upon the balloon part of the logo if you can.
I put one I was doing with a new balloon and a more "string-like" "I".

```html
<!DOCTYPE html>
<html lang="en">
<head>
<meta charset="utf-8">
<title>Harborlight Real Estate — Business Card</title>
<link rel="stylesheet" href="https://fonts.googleapis.com/css2?family=Open+Sans:wght@400;600&display=swap">
<style>
  :root {
    --navy-deep: #101848;
    --navy: #1b2866;
    --navy-glow: #2f57a8;
    --brand-green: #6fae3a;
    --ink: #222a3a;
    --muted: #4a4f5c;
    --paper: #ffffff;
    --backdrop: #eceae6;
  }
  * { margin: 0; padding: 0; box-sizing: border-box; }
  html, body { width: 1200px; height: 784px; overflow: hidden; }
  body {
    background: var(--backdrop);
    font-family: "Open Sans", Arial, sans-serif;
    position: relative;
  }
  .card {
    position: absolute;
    width: 560px;
    height: 320px;
    border-radius: 4px;
    overflow: hidden;
    box-shadow: 0 6px 18px rgba(0,0,0,0.18);
  }
  /* Back side */
  .card-back {
    left: 50px;
    top: 110px;
    background: radial-gradient(ellipse 60% 65% at 55% 40%, var(--navy-glow) 0%, var(--navy) 45%, var(--navy-deep) 100%);
  }
  .brand {
    display: flex;
    align-items: center;
    gap: 12px;
    font-weight: 600;
    letter-spacing: 0.04em;
    text-transform: uppercase;
  }
  .brand-dot {
    width: 22px; height: 22px;
    border-radius: 50%;
    background: var(--brand-green);
    flex: none;
  }
  .card-back .brand {
    position: absolute;
    left: 0; right: 0; top: 92px;
    justify-content: center;
    color: var(--paper);
    font-size: 30px;
    line-height: 1.1;
  }
  .brand-name { display: flex; flex-direction: column; }
  .brand-line-2 { font-size: 0.62em; letter-spacing: 0.32em; }
  .back-url {
    position: absolute;
    left: 0; right: 0; bottom: 38px;
    text-align: center;
    color: var(--paper);
    font-size: 15px;
    letter-spacing: 0.42em;
  }
  /* Front side */
  .card-front {
    left: 590px;
    top: 354px;
    background: var(--paper);
  }
  .card-front .brand {
    position: absolute;
    left: 34px; top: 52px;
    color: var(--navy);
    font-size: 28px;
    line-height: 1.1;
  }
  .person { position: absolute; left: 34px; top: 150px; }
  .person-name { color: var(--navy); font-size: 19px; font-weight: 600; }
  .person-title { color: var(--muted); font-size: 11px; margin-top: 1px; }
  .contact-list {
    position: absolute;
    left: 34px; top: 200px;
    list-style: none;
    color: var(--ink);
    font-size: 14px;
    line-height: 19px;
  }
  .contact-list li { display: flex; align-items: center; gap: 7px; }
  .contact-list svg { width: 13px; height: 13px; fill: var(--navy); flex: none; }
  .accent-line {
    position: absolute; left: 0; right: 0; bottom: 34px;
    height: 3px; background: var(--brand-green);
  }
  .base-band {
    position: absolute; left: 0; right: 0; bottom: 0;
    height: 34px; background: var(--navy-deep);
  }
</style>
</head>
<body>

<section class="card card-back" aria-label="Card back">
  <div class="brand">
    <span class="brand-dot"></span>
    <span class="brand-name"><span>Harborlight</span><span class="brand-line-2">Real Estate</span></span>
  </div>
  <p class="back-url">www.harborlightrealty.com</p>
</section>

<section class="card card-front" aria-label="Card front">
  <div class="brand">
    <span class="brand-dot"></span>
    <span class="brand-name"><span>Harborlight</span><span class="brand-line-2">Real Estate</span></span>
  </div>
  <div class="person">
    <p class="person-name">Marla Quenby</p>
    <p class="person-title">Owner/Realtor</p>
  </div>
  <ul class="contact-list">
    <li><svg viewBox="0 0 24 24" aria-hidden="true"><path d="M6.6 10.8a15 15 0 0 0 6.6 6.6l2.2-2.2a1 1 0 0 1 1-.25 11.4 11.4 0 0 0 3.6.57 1 1 0 0 1 1 1V20a1 1 0 0 1-1 1A17 17 0 0 1 3 4a1 1 0 0 1 1-1h3.5a1 1 0 0 1 1 1c0 1.25.2 2.45.57 3.57a1 1 0 0 1-.25 1z"/></svg>256-555-0148</li>
    <li><svg viewBox="0 0 24 24" aria-hidden="true"><path d="M12 2a10 10 0 1 0 0 20 10 10 0 0 0 0-20zm6.9 6h-2.9a15.6 15.6 0 0 0-1.4-3.6A8 8 0 0 1 18.9 8zM12 4c.8 1.2 1.5 2.5 1.9 4h-3.8c.4-1.5 1.1-2.8 1.9-4zM4.3 14a8 8 0 0 1 0-4h3.4a16.5 16.5 0 0 0 0 4zm.8 2h2.9c.3 1.3.8 2.5 1.4 3.6A8 8 0 0 1 5.1 16zM8 8H5.1a8 8 0 0 1 4.3-3.6C8.8 5.5 8.3 6.7 8 8zm4 12c-.8-1.2-1.5-2.5-1.9-4h3.8c-.4 1.5-1.1 2.8-1.9 4zm2.3-6H9.7a14.7 14.7 0 0 1 0-4h4.6a14.7 14.7 0 0 1 0 4zm.3 5.6c.6-1.1 1.1-2.3 1.4-3.6h2.9a8 8 0 0 1-4.3 3.6zm1.7-5.6a16.5 16.5 0 0 0 0-4h3.4a8 8 0 0 1 0 4z"/></svg>www.harborlightrealty.com</li>
    <li><svg viewBox="0 0 24 24" aria-hidden="true"><path d="M3 5h18a1 1 0 0 1 1 1v12a1 1 0 0 1-1 1H3a1 1 0 0 1-1-1V6a1 1 0 0 1 1-1zm1 2.2V17h16V7.2l-8 5.3z"/></svg>marlaquenby@mail.com</li>
    <li><svg viewBox="0 0 24 24" aria-hidden="true"><path d="M12 3l10 9h-3v8h-5v-6h-4v6H5v-8H2z"/></svg>214 Mercer Ave., Riverton, AL 35899</li>
  </ul>
  <div class="accent-line"></div>
  <div class="base-band"></div>
</section>

</body>
</html>
```